Stationery Design Project - Professional Training Company

Full set of statinery in PDF and format that can be given to the printers

Letterhead
Business cards x 3
Compliments slip
Envelope
Updates

Many thanks for all your contributions, the quality of the designs is amazing.

Thank you all so much for your contribution to this project, I am very impressed with the designs and choice of designs, you are all clearly very talented individuals.

I hope to be making a decision on the final choice this evening UAE time.

Best regards and again thank you so much

Gordon

I would like to take this opportunity to thank you all for your contributions, I have been very impressed with each of the designs submitted.

I will shortly go back and give each of you a personal rating on each of your designs.

Again thank you all so much for your efforts

Best Regards

Gordon

Target Market(s)

We are a training company that provides IT training for Medical and Professional Staff, we train professional adults

Industry/Entity Type

Business

Requirements
Must have
• The letterhead and compliments slip must have at the bottom of the page:-

Bright Ledger Pathways LLP operates as a limited liability partnership registered in England and Wales (with registered number OC702614)

Business Cards are to be made up for three people (details of those to be provided after appoval of design but are included in this project) and should contain:

Name
Title
Telephone
email
Address: P.O. Box 418263 Dubai UAE
web address: www.brightledgerpathways.example
Nice to have
• Very clean and professional looking
Should not have
• No look to busy or ovr crowded

```html
<!DOCTYPE html>
<html lang="en">
<head>
<meta charset="utf-8">
<title>Bright Ledger Pathways LLP – Business Card</title>
<link rel="stylesheet" href="https://fonts.googleapis.com/css2?family=Teko:wght@400;500&display=swap">
<style>
  :root {
    --ink: #2a0a26;
    --plum: #7b1f6c;
    --plum-light: #a0478f;
    --green: #4ea322;
    --header-top: #ececec;
    --header-bottom: #cbcbcb;
    --rule: #4a1040;
    --paper: #ffffff;
    --accent-text: #ffffff;
  }
  html, body {
    margin: 0;
    padding: 0;
    width: 1200px;
    height: 686px;
    overflow: hidden;
    background: var(--paper);
  }
  .card {
    position: relative;
    width: 1200px;
    height: 686px;
    background: var(--paper);
    font-family: "Teko", "Arial Narrow", sans-serif;
    color: var(--ink);
    overflow: hidden;
  }
  .card-header {
    position: absolute;
    left: 0; top: 0;
    width: 1200px;
    height: 212px;
    background: linear-gradient(to bottom, var(--header-top), var(--header-bottom));
    border-bottom: 3px solid var(--rule);
    display: flex;
    align-items: center;
    justify-content: center;
    gap: 22px;
  }
  .brand-dot {
    width: 62px;
    height: 62px;
    border-radius: 50%;
    background: var(--green);
  }
  .brand-name {
    font-weight: 500;
    font-size: 84px;
    line-height: 1;
    color: var(--ink);
    padding-top: 12px;
  }
  .accent-field {
    position: absolute;
    left: 440px;
    top: 215px;
    width: 760px;
    height: 471px;
    background: linear-gradient(135deg, var(--plum) 0%, var(--plum-light) 55%, var(--green) 100%);
  }
  .angled-line {
    position: absolute;
    margin: 0;
    font-weight: 500;
    font-size: 36px;
    line-height: 36px;
    height: 36px;
    white-space: nowrap;
    color: var(--accent-text);
    text-transform: uppercase;
    transform-origin: left bottom;
    transform: rotate(-37deg);
  }
  .angled-web { left: 500px; top: 572px; }
  .angled-address { left: 648px; top: 584px; }
  .person {
    position: absolute;
    left: 30px;
    top: 268px;
    text-transform: uppercase;
  }
  .person-name {
    margin: 0;
    font-weight: 500;
    font-size: 86px;
    line-height: 0.9;
  }
  .person-title {
    margin: 0;
    font-weight: 500;
    font-size: 56px;
    line-height: 0.9;
  }
  .contact {
    position: absolute;
    left: 30px;
    top: 496px;
    margin: 0;
    padding: 0;
    list-style: none;
    font-weight: 500;
    font-size: 58px;
    line-height: 1.4;
    text-transform: uppercase;
  }
</style>
</head>
<body>
<div class="card">
  <div class="accent-field" role="img" aria-label="Decorative purple and green brand artwork area"></div>

  <p class="angled-line angled-web">brightledgerpathways.example</p>
  <p class="angled-line angled-address">PO Box 418263 Dubai UAE</p>

  <header class="card-header">
    <span class="brand-dot"></span>
    <span class="brand-name">Bright Ledger Pathways LLP</span>
  </header>

  <section class="person">
    <h1 class="person-name">Name Surname</h1>
    <p class="person-title">Title Here</p>
  </section>

  <ul class="contact">
    <li class="contact-phone">(555) 555-5555</li>
    <li class="contact-email">email@email.com</li>
  </ul>
</div>
</body>
</html>
```